Business Card Design Project

We need a business card designed for a new Luxury Custom Homebuilding company based in Arizona. We previous were called "Brellcrest Estates" but want to start using "Brellcrest Custom Homes" We want the message to communicate high end, luxury and cutting-edge. We like the blue, white and black color scheme.
Brellcrest Custom Homes
Marcus T. Pellingham
Chief Executive Officer
Office: 480-555-0142
Mobile: 480-555-0173
email: marcus@brellcrestcustom.com
web adress: www.BrellcrestCustom.com
Updates
We have made a change to our website address and email address based on recieving feedback from a nmber of individuals. The feedback was web address and email address was to long. Therefore we have made a change. The new web adress and email adress are the following.
www.BrellcrestCustom.com
marcus@brellcrestcustom.com
Also I decided against using in yellow. I like the colors blue,black, white and maybe gray.
Target Market(s)
Our target market is the wealthy individuals looking for a luxury high-end custom home.
Industry/Entity Type
Business
Look and feel
Each slider illustrates characteristics of the customer's brand and the style your logo design should communicate.

```html
<!DOCTYPE html>
<html lang="en">
<head>
<meta charset="utf-8">
<title>Brellcrest Custom Homes – Business Card</title>
<link rel="stylesheet" href="https://fonts.googleapis.com/css2?family=Oswald:wght@600&family=PT+Sans:wght@400;700&display=swap">
<style>
  :root {
    --canvas: #ffffff;
    --charcoal: #383838;
    --charcoal-dark: #333333;
    --band-1: #454545;
    --band-2: #505050;
    --band-3: #5e5e5e;
    --ink: #3a3a3a;
    --blue: #5b9bd5;
    --white: #ffffff;
    --shadow: rgba(0, 0, 0, 0.45);
  }
  * { box-sizing: border-box; margin: 0; padding: 0; }
  html, body {
    width: 1200px;
    height: 1000px;
    overflow: hidden;
    background: var(--canvas);
  }
  .stage { position: relative; width: 1200px; height: 1000px; }

  .card {
    position: absolute;
    left: 283px;
    width: 660px;
    height: 376px;
    overflow: hidden;
    box-shadow: 3px 4px 6px var(--shadow);
  }
  .card--front { top: 93px; background: var(--charcoal); }
  .card--back { top: 533px; background: var(--white); }

  .card__bands { position: absolute; inset: 0; }

  .wordmark {
    position: absolute;
    font-family: "Oswald", "Arial Narrow", sans-serif;
    font-weight: 600;
    line-height: 1;
    letter-spacing: -0.5px;
  }
  .wordmark__name { display: block; font-size: 64px; }
  .wordmark__sub { display: block; font-size: 29px; letter-spacing: 0.5px; margin-top: 2px; padding-left: 98px; }
  .card--front .wordmark { left: 36px; top: 198px; color: var(--white); }
  .card--back .wordmark { left: 48px; top: 66px; color: var(--ink); }

  .web-front {
    position: absolute;
    left: 99px;
    top: 329px;
    font-family: "PT Sans", Arial, sans-serif;
    font-size: 17px;
    letter-spacing: 0.6px;
    color: var(--white);
  }
  .web-front .accent { color: var(--blue); }

  .edge-tab {
    position: absolute;
    left: -12px;
    top: 250px;
    width: 27px;
    height: 48px;
    border-radius: 8px;
    background: var(--charcoal-dark);
  }

  .person { position: absolute; left: 49px; top: 250px; font-family: "PT Sans", Arial, sans-serif; }
  .person__name { font-size: 21px; font-weight: 700; color: var(--blue); letter-spacing: 0.2px; }
  .person__title { font-size: 16px; color: var(--ink); margin-top: 4px; }

  .contact {
    position: absolute;
    left: 383px;
    top: 241px;
    list-style: none;
    font-family: "PT Sans", Arial, sans-serif;
    font-size: 16.5px;
    color: var(--ink);
  }
  .contact li { display: flex; align-items: center; height: 22px; }
  .contact svg { width: 17px; height: 16px; margin-right: 7px; fill: var(--blue); }

  .footer-bar { position: absolute; left: 0; bottom: 0; width: 660px; height: 44px; }
  .web-back {
    position: absolute;
    right: 36px;
    bottom: 15px;
    font-family: "PT Sans", Arial, sans-serif;
    font-size: 17px;
    letter-spacing: 0.8px;
    color: var(--white);
  }
</style>
</head>
<body>
<main class="stage">

  <section class="card card--front" aria-label="Card front">
    <svg class="card__bands" viewBox="0 0 660 376" preserveAspectRatio="none" aria-hidden="true">
      <path d="M0 40 C200 95 430 60 550 0 L660 0 L660 75 C520 140 250 160 0 140 Z" fill="var(--band-1)"/>
      <path d="M0 140 C250 160 520 140 660 75 L660 150 C500 200 250 215 0 200 Z" fill="var(--band-2)"/>
      <path d="M0 200 C250 215 500 200 660 150 L660 220 C480 245 250 250 0 245 Z" fill="var(--band-3)" opacity="0.8"/>
      <path d="M0 245 C250 250 480 245 660 220 L660 290 C460 300 250 300 0 295 Z" fill="var(--band-1)"/>
    </svg>
    <div class="wordmark">
      <span class="wordmark__name">Brellcrest</span>
      <span class="wordmark__sub">CUSTOM HOMES</span>
    </div>
    <p class="web-front">www.Brellcrest<span class="accent">Custom</span>.com</p>
  </section>

  <section class="card card--back" aria-label="Card back">
    <div class="wordmark">
      <span class="wordmark__name">Brellcrest</span>
      <span class="wordmark__sub">CUSTOM HOMES</span>
    </div>

    <div class="edge-tab" aria-hidden="true"></div>

    <div class="person">
      <p class="person__name">Marcus T. Pellingham</p>
      <p class="person__title">Chief Executive Officer</p>
    </div>

    <ul class="contact">
      <li>
        <svg viewBox="0 0 17 16" aria-hidden="true"><path d="M1 5 C1 2 5 1 8.5 1 S16 2 16 5 L13 6 L12 4 C10 3.4 7 3.4 5 4 L4 6 Z M4 8 L13 8 L15 15 L2 15 Z M8.5 9.5 A2.3 2.3 0 1 0 8.51 9.5 Z"/></svg>
        480-555-0142
      </li>
      <li>
        <svg viewBox="0 0 17 16" aria-hidden="true"><path d="M5 0 H12 A1.5 1.5 0 0 1 13.5 1.5 V14.5 A1.5 1.5 0 0 1 12 16 H5 A1.5 1.5 0 0 1 3.5 14.5 V1.5 A1.5 1.5 0 0 1 5 0 Z M5 2 V12.5 H12 V2 Z M8.5 13.2 A1 1 0 1 0 8.51 13.2 Z"/></svg>
        480-555-0173
      </li>
      <li>
        <svg viewBox="0 0 17 16" aria-hidden="true"><path d="M0 3 H17 V13 H0 Z M1.2 4 L8.5 9.3 L15.8 4 Z M1 12 H16 L11 7.8 L8.5 9.8 L6 7.8 Z"/></svg>
        marcus@brellcrestcustom.com
      </li>
    </ul>

    <svg class="footer-bar" viewBox="0 0 660 44" aria-hidden="true">
      <path d="M0 24 H328 L318 44 H0 Z" fill="var(--charcoal-dark)"/>
      <path d="M328 44 L348 14 C353 6 360 1 372 1 H660 V44 Z" fill="var(--blue)"/>
    </svg>
    <p class="web-back">www.BrellcrestCustom.com</p>
  </section>

</main>
</body>
</html>
```